Private vineyard wine bottle label design

We need a label for our private vineyard's wine in La Cresta California. The wine will not be for sale, so there are no legal requirements about what can or cannot be on the label. We would like the name of the vineyard "Harrow Vine Groves" displayed prominently, and to also include
the grape type "Barbera", and optionally the vineyard location. We would like a stylized (but not cartoonish) image of a stoic bull with horns included. I would also like to hide the image of a maple leaf somewhere on the label, it should be subtle and not obvious unless someone is specifically looking for it. We would like a muted color palate, with a light background.

```html
<!DOCTYPE html>
<html lang="en">
<head>
<meta charset="utf-8">
<title>Harrow Vine Groves – Barbera Label</title>
<link rel="stylesheet" href="https://fonts.googleapis.com/css2?family=Cinzel:wght@400&family=Cormorant+Garamond:wght@500&display=swap">
<style>
  :root {
    --page: #f4f4f2;
    --mint: #c3ebdf;
    --mint-light: #dcf4ec;
    --mint-deep: #a9dccd;
    --wine: #b0525a;
    --ink: #262626;
    --bull-tone: #6f7f7b;
    --leaf-tone: #e3ecd9;
  }
  * { margin: 0; padding: 0; box-sizing: border-box; }
  html, body {
    width: 1200px;
    height: 1152px;
    overflow: hidden;
    background: var(--page);
  }
  .canvas {
    position: relative;
    width: 1200px;
    height: 1152px;
  }
  .label {
    position: absolute;
    left: 210px;
    top: 56px;
    width: 780px;
    height: 1040px;
    overflow: hidden;
    background:
      linear-gradient(90deg, transparent 0 28%, rgba(150,190,180,.18) 28% 34%, transparent 34% 62%, rgba(150,190,180,.16) 62% 67%, transparent 67%),
      radial-gradient(ellipse at 60% 25%, var(--mint-light) 0%, transparent 45%),
      radial-gradient(ellipse at 30% 70%, var(--mint-deep) 0%, transparent 55%),
      var(--mint);
    box-shadow: 0 2px 14px rgba(0,0,0,.08);
    font-family: "Cinzel", serif;
    text-align: center;
  }
  .art {
    position: absolute;
    border-radius: 40% 50% 45% 55%;
  }
  .art--bull {
    left: 250px;
    top: 63px;
    width: 266px;
    height: 510px;
    background: radial-gradient(ellipse at 50% 55%, var(--bull-tone) 0%, rgba(111,127,123,.55) 55%, rgba(111,127,123,0) 75%);
  }
  .art--leaf-top {
    left: -20px;
    top: 131px;
    width: 192px;
    height: 285px;
    background: radial-gradient(ellipse, rgba(255,255,255,.55) 0%, rgba(255,255,255,0) 70%);
  }
  .art--leaf-bottom {
    left: 565px;
    top: 612px;
    width: 220px;
    height: 274px;
    background: radial-gradient(ellipse, var(--leaf-tone) 0%, rgba(227,236,217,0) 72%);
  }
  .brand {
    position: absolute;
    left: 0;
    right: 0;
    top: 440px;
    color: var(--wine);
    font-weight: 400;
  }
  .brand__name {
    display: block;
    font-size: 104px;
    line-height: 1;
    letter-spacing: 4px;
  }
  .brand__sub {
    display: block;
    margin-top: 34px;
    font-size: 38px;
    letter-spacing: 9px;
  }
  .varietal {
    position: absolute;
    left: 0;
    right: 0;
    top: 758px;
    font-family: "Cormorant Garamond", serif;
    font-weight: 500;
    font-size: 46px;
    letter-spacing: 9px;
    color: var(--ink);
  }
  .origin {
    position: absolute;
    left: 0;
    right: 0;
    top: 892px;
    color: var(--ink);
  }
  .origin__intro {
    display: block;
    font-size: 19px;
    letter-spacing: 6px;
  }
  .origin__place {
    display: block;
    margin-top: 14px;
    font-size: 31px;
    line-height: 1.1;
    letter-spacing: 5px;
    color: var(--wine);
  }
  .spec {
    position: absolute;
    top: 988px;
    font-family: "Cormorant Garamond", serif;
    font-size: 20px;
    letter-spacing: 2px;
    color: var(--ink);
  }
  .spec--volume { left: 62px; }
  .spec--abv { right: 62px; }
</style>
</head>
<body>
<main class="canvas">
  <section class="label">
    <div class="art art--leaf-top" role="img" aria-label="Faint line drawing of a maple leaf"></div>
    <div class="art art--bull" role="img" aria-label="Stylized watercolour silhouette of a stoic horned bull"></div>
    <div class="art art--leaf-bottom" role="img" aria-label="Pale watercolour maple leaf"></div>

    <h1 class="brand">
      <span class="brand__name">Harrow</span>
      <span class="brand__sub">VINE GROVES</span>
    </h1>

    <p class="varietal">BARBERA</p>

    <p class="origin">
      <span class="origin__intro">VINEYARD'S WINE IN</span>
      <span class="origin__place">LA CRESTA<br>CALIFORNIA</span>
    </p>

    <p class="spec spec--volume">750ML</p>
    <p class="spec spec--abv">13%VOL</p>
  </section>
</main>
</body>
</html>
```